Australian Craft Distillery needs poster layout for its awesome Manifesto

Tall Finch's a small craft distillery based in the Brook Flats of Western Australia producing award-winning vodkas and gin. Check out our website www.tallfinchs-example.com.au to get a feel for our design aesthetic, especially from our bottle design. We are "Small Batch Liquors - Out of the Brook Flats". Everything we do reflects that.
We have a manifesto - The Tall Finch's Manifesto -that we proudly display in our tasting room, and was used as a basis for an artwork in our entry.
We've had a number of customers ask to buy a poster of the manifesto (attached) so I want to commission a more professional design than the current layout which was put together in Word! (yes I know, I'm sorry, I did move it into Illustrator later).
I think the text flows in a sequential order so I'm looking for a design that you read from start to finish rather than a random collection of statements. I'd like to include our logo in the design somewhere but it doesn't have to be front and centre. There is a secondary logo device as well - the interlocked T and F on the label which could be used. I'm assuming the print will be simple black on either a plain background or a "craft background" similar to the labels. Our current fonts are SchmutzICG for text and VeneerTwo for headings. The label uses Haymaker and Gin-Rough.
Print size will be A3 (prefer the design to be to this proportion and portrait orientation) and bigger up to A1. We'll print the final design on the back of t-shirts for staff as well. If I was going to sum up our style in a couple of words it would be "intelligently irreverent" Have fun with this, I certainly did writing it!

```html
<!DOCTYPE html>
<html lang="en">
<head>
<meta charset="utf-8">
<title>The Tall Finch's Manifesto</title>
<link rel="stylesheet" href="https://fonts.googleapis.com/css2?family=Anton&family=Oswald:wght@500;700&family=Special+Elite&display=swap">
<style>
  :root {
    --paper: #f2f0eb;
    --ink: #221f1f;
    --rule: #221f1f;
  }
  * { box-sizing: border-box; margin: 0; padding: 0; }
  html, body { width: 874px; height: 1200px; overflow: hidden; }
  body {
    background: var(--paper);
    color: var(--ink);
    font-family: "Special Elite", "Courier New", monospace;
  }
  .poster {
    width: 874px; height: 1200px;
    padding: 44px 62px 0;
    display: flex; flex-direction: column; align-items: center;
  }
  .brand-top { display: flex; flex-direction: column; align-items: center; gap: 6px; }
  .brand-square { width: 26px; height: 26px; background: var(--ink); }
  .brand-name {
    font-family: "Oswald", sans-serif; font-weight: 700;
    font-size: 11px; letter-spacing: 3px; text-transform: uppercase;
  }
  .title-small {
    margin-top: 22px;
    font-family: "Anton", sans-serif; font-size: 50px; line-height: 1;
    letter-spacing: 1px; text-transform: uppercase;
  }
  .title-big {
    font-family: "Anton", sans-serif; font-size: 138px; line-height: 1;
    letter-spacing: 6px; text-transform: uppercase; margin-top: 2px;
  }
  .subtitle {
    width: 100%; text-align: center; margin-top: 8px;
    border-top: 3px solid var(--rule); border-bottom: 1px solid var(--rule);
    padding: 7px 0 6px;
    font-family: "Oswald", sans-serif; font-weight: 500;
    font-size: 17px; letter-spacing: 2.5px; text-transform: uppercase;
  }
  .section {
    width: 100%;
    padding: 14px 0 12px;
    border-bottom: 1px dashed var(--rule);
    font-size: 17.5px; line-height: 27px;
    text-transform: uppercase; text-align: justify;
  }
  .section-label {
    float: left;
    font-family: "Anton", sans-serif; font-size: 56px; line-height: 54px;
    margin: 0 14px 0 0; letter-spacing: 1px;
  }
  .section-label.is-small { font-size: 34px; line-height: 30px; margin-top: -2px; }
  .section--of-course { display: flex; align-items: center; gap: 20px; }
  .section--of-course .section-label { float: none; margin: 0; }
  .of-course-text { font-size: 18px; }
  .closing {
    width: 100%; text-align: center; margin-top: 14px;
    border-top: 3px solid var(--rule); border-bottom: 3px solid var(--rule);
    padding: 8px 0 6px;
    font-family: "Oswald", sans-serif; font-weight: 700;
    font-size: 21px; letter-spacing: 2px; text-transform: uppercase;
  }
  .brand-bottom {
    margin-top: 20px; display: flex; flex-direction: column; align-items: center; gap: 5px;
  }
  .brand-bottom .brand-square { width: 30px; height: 30px; border-radius: 50%; }
  .brand-tagline {
    font-family: "Oswald", sans-serif; font-weight: 500;
    font-size: 9px; letter-spacing: 2px; text-transform: uppercase;
  }
</style>
</head>
<body>
<main class="poster">
  <header class="brand-top">
    <span class="brand-square" aria-hidden="true"></span>
    <span class="brand-name">Tall Finch's</span>
  </header>

  <h1>
    <span class="title-small" style="display:block;text-align:center">The Tall Finch's</span>
    <span class="title-big" style="display:block;text-align:center">Manifesto</span>
  </h1>
  <p class="subtitle">Our thoughts on life a.k.a. how to be better</p>

  <section class="section">
    <h2 class="section-label">FIRST</h2>
    <p>Work smart · Love hard · Play often · Sleep more · Stay present · Be local · Embrace silly · Get dirty (but) stay clean · Laugh! · Cry · Run · Dance · Sing · Stop that (and) slow down</p>
  </section>

  <section class="section">
    <h2 class="section-label">THEN</h2>
    <p>Celebrate other's success · Don't be shit · Have one thing you are awesome at · Get off your phone · Show some fucking passion · Make something · Making money doesn't count · Making babies does · Never stop exploring, never stop learning, share that with others · We all fuck up · Make good, learn, be better · And move on</p>
  </section>

  <section class="section section--of-course">
    <h2 class="section-label is-small">...AND OF COURSE</h2>
    <p class="of-course-text">Drink better</p>
  </section>

  <section class="section">
    <h2 class="section-label is-small">...AND FINALLY</h2>
    <p>Sometimes you just won't understand · An argument is not a fight · You are not as important as you think · You are more loved than you think · Its ok to do things alone · Its ok not to be busy · There is no good reason to do a half assed job · Teaching is the best way of learning · The past is important, what you do next is much more so · Change is inevitable, roll with it · Success is whatever you decide it to be</p>
  </section>

  <p class="closing">Life is far too short. Squeeze every drop out of it</p>

  <footer class="brand-bottom">
    <span class="brand-square" aria-hidden="true"></span>
    <span class="brand-name">Tall Finch's</span>
    <span class="brand-tagline">Small Batch Liquors - Out of the Brook Flats</span>
  </footer>
</main>
</body>
</html>
```